New look while maintaining the Brand identification!

I want a new look for my business card. I want to keep the same colors and feel but change the look and layout a bit. The logo (KALMORETIX Physical therapy Reimagined and the lilypad) must remain the same and in that font.
We are a physical therapy clinic. So we have certification that we can write on the back or services we provide (which is what we currently have on the back of the card as well)

Contact information
2840 Cedar Hollow Rd., #22
Naples, FL 34276
P: (239) 555-0172
F: (239) 555-0198
E: kalmoretixcare@mailvexo.com
W: www.kalmoretixcare-example.com

Industry/Entity Type

Physical Therapy

Contact Information for Business Card

Our current cards have the business address and information on the back. But I am willing to have it be in the front.

Font styles to use
Sans Serif

Colors
abd036
fbf289
ec1f27

Requirements
Must have
• Has to be unique!
• Services we provide and/or techniques we do must fit on the card
Nice to have
• Would like to have the front and back somehow linked together. Such that if you set the front next to the back, there is a nice flow of design! Currently the back is white with writing on it.
Should not have
• I like the wave lines as compared to straight lines.

```html
<!DOCTYPE html>
<html lang="en">
<head>
<meta charset="utf-8">
<title>Kalmoretix Business Card</title>
<link rel="stylesheet" href="https://fonts.googleapis.com/css2?family=Oswald:wght@500&family=Open+Sans:wght@400&display=swap">
<style>
  :root {
    --backdrop: #efeff0;
    --card: #eaebec;
    --brand-gold: #d4b629;
    --wave-yellow: #f3e55c;
    --wave-green: #c8cb4c;
    --floral-tint: #dfe0e2;
    --ink: #1c1c1c;
  }
  * { box-sizing: border-box; margin: 0; padding: 0; }
  html, body { width: 1200px; height: 420px; overflow: hidden; }
  body {
    background: var(--backdrop);
    position: relative;
    font-family: "Open Sans", Arial, sans-serif;
  }
  .card {
    position: absolute;
    width: 492px;
    height: 284px;
    background: var(--card);
    overflow: hidden;
  }
  .card--front { left: 68px; top: 74px; }
  .card--back { left: 640px; top: 72px; }

  .floral-texture {
    position: absolute;
    inset: 0;
    background:
      radial-gradient(ellipse at 10% 10%, var(--floral-tint) 0%, transparent 45%),
      radial-gradient(ellipse at 85% 90%, var(--floral-tint) 0%, transparent 50%);
  }

  .brand-name {
    position: absolute;
    font-family: "Oswald", "Arial Narrow", sans-serif;
    font-weight: 500;
    color: var(--brand-gold);
    letter-spacing: 0.5px;
    line-height: 1;
    white-space: nowrap;
  }
  .card--front .brand-name {
    left: 0; right: 0;
    top: 128px;
    text-align: center;
    font-size: 44px;
  }
  .card--back .brand-name {
    right: 26px;
    top: 46px;
    font-size: 35px;
  }

  .wave { position: absolute; left: 0; top: 0; width: 492px; height: 284px; }

  .contact-list {
    position: absolute;
    left: 18px;
    top: 44px;
    list-style: none;
    color: var(--ink);
    font-size: 13px;
    line-height: 18px;
  }
  .contact-item {
    display: flex;
    align-items: flex-start;
    gap: 12px;
    margin-bottom: 14px;
  }
  .contact-icon { width: 16px; height: 16px; flex: none; margin-top: 1px; fill: var(--ink); }
</style>
</head>
<body>

  <section class="card card--front">
    <div class="floral-texture" role="img" aria-label="Faint floral leaf pattern across the card"></div>
    <div class="brand-name">KALMORETIX</div>
  </section>

  <section class="card card--back">
    <svg class="wave" viewBox="0 0 492 284" role="img" aria-label="Yellow and green wave band with leaf texture">
      <path d="M0 254 C 120 300, 200 220, 280 160 C 350 110, 420 98, 492 100 L492 284 L0 284 Z" fill="var(--wave-yellow)"/>
      <path d="M0 270 C 120 306, 210 240, 290 180 C 360 132, 430 122, 492 124 L492 284 L0 284 Z" fill="var(--wave-green)"/>
    </svg>

    <div class="brand-name">KALMORETIX</div>

    <ul class="contact-list">
      <li class="contact-item">
        <svg class="contact-icon" viewBox="0 0 16 16"><path d="M8 1a5 5 0 0 0-5 5c0 4 5 9 5 9s5-5 5-9a5 5 0 0 0-5-5zm0 7a2 2 0 1 1 0-4 2 2 0 0 1 0 4z"/></svg>
        <span>2840 Cedar Hollow Rd., #22<br>Naples, FL 34276</span>
      </li>
      <li class="contact-item">
        <svg class="contact-icon" viewBox="0 0 16 16"><path d="M4 1l2.5 3-1.5 2c1 2 3 4 5 5l2-1.5 3 2.5-1.5 2.5C8 15 1 8 1.5 2.5z"/></svg>
        <span>(239) 555-0172</span>
      </li>
      <li class="contact-item">
        <svg class="contact-icon" viewBox="0 0 16 16"><path d="M2 4h3v10H2zM6 2h6l2 2v10H6zm2 5v2h2V7zm3 0v2h2V7zm-3 3v2h2v-2zm3 0v2h2v-2z"/></svg>
        <span>(239) 555-0198</span>
      </li>
      <li class="contact-item">
        <svg class="contact-icon" viewBox="0 0 16 16"><path d="M1 4h14v1L8 9 1 5zm0 2.5l7 4 7-4V13H1z"/></svg>
        <span>kalmoretixcare@mailvexo.com</span>
      </li>
      <li class="contact-item">
        <svg class="contact-icon" viewBox="0 0 16 16"><path d="M8 1a7 7 0 1 0 0 14A7 7 0 0 0 8 1zm5 6h-2.6a11 11 0 0 0-1-4.2A5.5 5.5 0 0 1 13 7zM8 2.6c.7.9 1.2 2.6 1.3 4.4H6.7C6.8 5.2 7.3 3.5 8 2.6zM6.6 2.8A11 11 0 0 0 5.6 7H3a5.5 5.5 0 0 1 3.6-4.2zM3 9h2.6a11 11 0 0 0 1 4.2A5.5 5.5 0 0 1 3 9zm5 4.4c-.7-.9-1.2-2.6-1.3-4.4h2.6c-.1 1.8-.6 3.5-1.3 4.4zm1.4-.2a11 11 0 0 0 1-4.2H13a5.5 5.5 0 0 1-3.6 4.2z"/></svg>
        <span>www.kalmoretixcare-example.com</span>
      </li>
    </ul>
  </section>

</body>
</html>
```